Non-Fiction Book Cover Series Concepts

I need front cover concepts for a non-fiction business book series. Just concepts at this stage to show to backers (full cover designs later).

The books are for leaders and business owners. A mature, sophisticated market, AND, bold and innovative.

The series needs to be extensible - the concepts need to be able to work across at least 40 books. I am happy with a colour theme, or contrasts, or icon theme, there is no limitation to the imagination.

The books need to look like they belong to a series and to also stand alone.

I prefer simple and bold.

Imagine the Heron business series (https://www.heronbooks-example.co.uk/series/lbs/heron-leaders-masters-series.html) - but I hate these designs (the colours don't work for me).

The imprint is ThoughtfulHorizon.example - the logo mark for the imprint is attached.

The books will be printed and ebooks - the printed version will be 5 inches by 8 inches form factor. They will be printed with a matt cover.

IF YOU WANT A BOOK TITLE TO TRY, use this:

Steady Momentum: Apply the R.A.F. Model to Nurture, Unlock and Keep Talent

Thank you for your interest!

Target Market(s)

Business owners, leaders, entrepreneurs

Industry/Entity Type

Leadership

Font styles to use
Serif
Sans Serif

Requirements
Must have
• Extensible - the concept can work for many books and ALL books look part of the series
Nice to have
• I prefer simple, icons rather than photos
Should not have
• No photographic designs - icon, drawing

```html
<!DOCTYPE html>
<html lang="en">
<head>
<meta charset="utf-8">
<title>Leaders and Business Owners — Series Cover Concepts</title>
<link rel="stylesheet" href="https://fonts.googleapis.com/css2?family=Bebas+Neue&family=Oswald:wght@300&display=swap">
<style>
  :root {
    --backdrop: #a9a9a9;
    --paper: #ffffff;
    --ink-dark: #3a3a3a;
    --orange: #ffa200;
    --orange-light: #ffbb3a;
    --orange-ink: #c9780a;
    --violet: #d77bee;
    --violet-light: #e6a6f4;
    --violet-ink: #7a3f8c;
    --sky: #00a6e8;
    --sky-light: #17c0ef;
    --sky-ink: #0b6b93;
    --arrow-pink: #ff8cf5;
    --arrow-cyan: #1ad6f2;
    --icon-pink: #f36bb5;
    --icon-blue: #2fa8f0;
    --icon-violet: #c23cf2;
  }
  * { box-sizing: border-box; margin: 0; padding: 0; }
  html, body { width: 800px; height: 1200px; overflow: hidden; }
  body { background: var(--backdrop); position: relative; }

  .series { position: relative; width: 800px; height: 1200px; }

  .cover {
    position: absolute;
    width: 240px;
    height: 370px;
    background: var(--paper);
    display: flex;
    box-shadow: 0 6px 16px rgba(0,0,0,0.18);
  }
  .cover--orange { left: 130px; top: 22px;  --accent: var(--orange); --accent-light: var(--orange-light); --title-ink: var(--orange-ink); }
  .cover--violet { left: 430px; top: 415px; --accent: var(--violet); --accent-light: var(--violet-light); --title-ink: var(--violet-ink); }
  .cover--sky    { left: 130px; top: 808px; --accent: var(--sky);    --accent-light: var(--sky-light);    --title-ink: var(--sky-ink); }

  .cover__front {
    flex: 0 0 156px;
    position: relative;
    padding: 14px 0 0 12px;
  }
  .cover__title {
    font-family: "Bebas Neue", "Oswald", sans-serif;
    font-weight: 400;
    font-size: 41px;
    line-height: 0.9;
    letter-spacing: -0.5px;
    text-transform: uppercase;
    background: linear-gradient(180deg, var(--ink-dark) 20%, var(--title-ink) 90%);
    -webkit-background-clip: text;
    background-clip: text;
    color: transparent;
  }
  .cover__icon {
    position: absolute;
    left: 14px;
    top: 178px;
    width: 120px;
    height: 110px;
    border-radius: 10px;
    background: linear-gradient(135deg, var(--icon-blue) 0%, var(--icon-violet) 55%, var(--icon-pink) 100%);
    opacity: 0.55;
  }
  .cover__author {
    position: absolute;
    left: 12px;
    bottom: 18px;
    font-family: "Oswald", sans-serif;
    font-weight: 300;
    font-size: 11px;
    letter-spacing: -0.2px;
    text-transform: uppercase;
    color: var(--title-ink);
  }
  .cover--orange .cover__author { color: var(--orange); }
  .cover--violet .cover__author { color: var(--violet); }

  .cover__band {
    flex: 1;
    position: relative;
    background: linear-gradient(160deg, var(--accent-light) 0%, var(--accent) 45%, var(--accent) 100%);
  }
  .cover__arrow {
    position: absolute;
    left: 50%;
    bottom: 0;
    width: 50px;
    height: 96px;
    transform: translateX(-50%);
  }
</style>
</head>
<body>
<svg width="0" height="0" style="position:absolute" aria-hidden="true">
  <defs>
    <linearGradient id="arrow-shaft" x1="0" y1="0" x2="0" y2="1">
      <stop offset="0" stop-color="#ff8cf5"/>
      <stop offset="0.6" stop-color="#c7a4fb"/>
      <stop offset="1" stop-color="#1ad6f2"/>
    </linearGradient>
  </defs>
</svg>

<main class="series">
  <article class="cover cover--orange">
    <div class="cover__front">
      <h1 class="cover__title">Leaders<br>and<br>Business<br>Owners</h1>
      <div class="cover__icon" role="img" aria-label="Line icon of a monitor with a gear and rising growth chart"></div>
      <p class="cover__author">Author Name</p>
    </div>
    <div class="cover__band">
      <svg class="cover__arrow" viewBox="0 0 50 96" aria-hidden="true">
        <path d="M25 6 V96" stroke="url(#arrow-shaft)" stroke-width="5" fill="none"/>
        <path d="M6 25 L25 6 L44 25" stroke="#ff8cf5" stroke-width="5" stroke-linecap="round" stroke-linejoin="round" fill="none"/>
      </svg>
    </div>
  </article>

  <article class="cover cover--violet">
    <div class="cover__front">
      <h1 class="cover__title">Leaders<br>and<br>Business<br>Owners</h1>
      <div class="cover__icon" role="img" aria-label="Line icon of a handshake beneath a tick and rising chart"></div>
      <p class="cover__author">Author Name</p>
    </div>
    <div class="cover__band">
      <svg class="cover__arrow" viewBox="0 0 50 96" aria-hidden="true">
        <path d="M25 6 V96" stroke="url(#arrow-shaft)" stroke-width="5" fill="none"/>
        <path d="M6 25 L25 6 L44 25" stroke="#ff8cf5" stroke-width="5" stroke-linecap="round" stroke-linejoin="round" fill="none"/>
      </svg>
    </div>
  </article>

  <article class="cover cover--sky">
    <div class="cover__front">
      <h1 class="cover__title">Leaders<br>and<br>Business<br>Owners</h1>
      <div class="cover__icon" role="img" aria-label="Line icon of a hand holding a money bag with coins"></div>
      <p class="cover__author">Author Name</p>
    </div>
    <div class="cover__band">
      <svg class="cover__arrow" viewBox="0 0 50 96" aria-hidden="true">
        <path d="M25 6 V96" stroke="url(#arrow-shaft)" stroke-width="5" fill="none"/>
        <path d="M6 25 L25 6 L44 25" stroke="#ff8cf5" stroke-width="5" stroke-linecap="round" stroke-linejoin="round" fill="none"/>
      </svg>
    </div>
  </article>
</main>
</body>
</html>
```